YARD CRAFTERS "N" CO

catyering to driveway/patio floor construction and remodeling. Concrete, concrete pavers, asphalt, Landscaping, irrigation, pergolas and pools.

Target Market(s)

the home owner that wants to enhance their home

Industry/Entity Type

construction

Contact Information for Business Card

presidet: lino barrega email: yardcraftersnco@mailbox.test office/cell: 555 204 8813

Font styles to use
Sans Serif

Requirements
Must have
• logo should pop out
Nice to have
• the logo should demonstrate that we do exteriors only

```html
<!DOCTYPE html>
<html lang="en">
<head>
<meta charset="utf-8">
<title>Yard Crafters "N" Co — Business Card</title>
<link href="https://fonts.googleapis.com/css2?family=Lato:wght@400;700;900&display=swap" rel="stylesheet">
<style>
  :root {
    --stage: #2b2b2d;
    --brand-blue: #1a8abb;
    --accent-gold: #d9900f;
    --paper: #ffffff;
    --ink: #1e1e1e;
  }
  * { box-sizing: border-box; margin: 0; padding: 0; }
  html, body {
    width: 1200px; height: 875px; overflow: hidden;
    background: var(--stage);
    font-family: "Lato", sans-serif;
  }
  .stage {
    position: relative; width: 1200px; height: 875px;
    display: flex; align-items: center; justify-content: center; gap: 40px;
  }
  .card {
    width: 520px; height: 300px; border-radius: 26px;
    position: relative; overflow: hidden;
  }
  .card--front {
    background: var(--brand-blue);
    display: flex; align-items: center; justify-content: center;
  }
  .wordmark {
    color: var(--paper); font-weight: 900; text-transform: uppercase;
    font-size: 40px; line-height: 1.05; letter-spacing: 0.5px;
    display: flex; align-items: center; gap: 16px;
  }
  .wordmark__mark {
    width: 22px; height: 22px; background: currentColor; flex: none;
  }
  .card--back { background: var(--paper); }
  .card--back .wordmark {
    color: var(--brand-blue); font-size: 24px; gap: 10px;
    position: absolute; left: 30px; bottom: 62px;
  }
  .card--back .wordmark__mark { width: 14px; height: 14px; }
  .contact {
    position: absolute; left: 280px; top: 48px; color: var(--ink);
  }
  .contact__name {
    color: var(--brand-blue); font-weight: 900; font-size: 24px;
    text-transform: uppercase; letter-spacing: 0.3px;
  }
  .contact__title {
    color: var(--accent-gold); font-size: 15px; font-weight: 700; margin-top: 2px;
  }
  .contact__rule {
    width: 40px; height: 2px; background: var(--brand-blue); margin: 10px 0 14px;
  }
  .contact__list { list-style: none; font-size: 12px; }
  .contact__item { display: flex; gap: 8px; align-items: flex-start; margin-bottom: 7px; line-height: 1.3; }
  .contact__item svg { width: 12px; height: 12px; flex: none; margin-top: 2px; fill: var(--accent-gold); }
  .contact__phone { font-size: 17px; }
</style>
</head>
<body>
  <main class="stage">
    <section class="card card--front" aria-label="Card front">
      <div class="wordmark"><span class="wordmark__mark"></span><span>Yard Crafters<br>"N" Co</span></div>
    </section>

    <section class="card card--back" aria-label="Card back">
      <div class="wordmark"><span class="wordmark__mark"></span><span>Yard Crafters<br>"N" Co</span></div>
      <div class="contact">
        <p class="contact__name">Lino Barrega</p>
        <p class="contact__title">Presidet</p>
        <div class="contact__rule"></div>
        <ul class="contact__list">
          <li class="contact__item">
            <svg viewBox="0 0 12 12"><path d="M6 0a4 4 0 0 0-4 4c0 3 4 8 4 8s4-5 4-8a4 4 0 0 0-4-4zm0 5.5A1.5 1.5 0 1 1 6 2.5a1.5 1.5 0 0 1 0 3z"/></svg>
            <span>4870 Elmridge Ct<br>#214 Harlow, Fla. 30412-7781</span>
          </li>
          <li class="contact__item">
            <svg viewBox="0 0 12 12"><path d="M2.5 0.5l2 2.5-1.2 1.3a7 7 0 0 0 4.4 4.4L9 7.5l2.5 2-1.5 2C5 11.5 0.5 7 0.5 2z"/></svg>
            <span class="contact__phone">555 204 8813</span>
          </li>
          <li class="contact__item">
            <svg viewBox="0 0 12 12"><path d="M0 2h12v8H0zM0.8 2.8v0.5L6 6.8l5.2-3.5v-0.5z" fill-rule="evenodd"/></svg>
            <span>yardcraftersnco@mailbox.test</span>
          </li>
        </ul>
      </div>
    </section>
  </main>
</body>
</html>
```